UK Online Auction Site needs a clever design

We need a contemporary landing page and registration page design for a UK auction website, that look equally at home on PC's and tablets . The design should be fresh, bright, clean, professional, robust, and familiar. We would like to see something clever but functional.

Industry/Entity Type

Online

```html
<!DOCTYPE html>
<html lang="en">
<head>
<meta charset="utf-8">
<title>Bidwell – UK Online Auctions</title>
<link href="https://fonts.googleapis.com/css2?family=Open+Sans:wght@400;600&family=Roboto+Condensed:wght@300;400;700&family=Roboto:wght@300;400&display=swap" rel="stylesheet">
<style>
:root{
  --blue:#1a8ad4;
  --blue-dark:#0f74b8;
  --green:#7cc21a;
  --green-dark:#5fa10c;
  --orange:#f7a21b;
  --ink:#333;
  --muted:#666;
  --pink:#f7d4ec;
  --footer:#1e1e1e;
  --footer-text:#cfcfcf;
  --caption:rgba(20,20,20,.82);
}
*{box-sizing:border-box;margin:0;padding:0}
html,body{width:740px;height:1200px;overflow:hidden;background:#fff}
body{font-family:"Open Sans",sans-serif;color:var(--ink);position:relative}
.abs{position:absolute}

/* header */
.header{position:absolute;left:0;top:0;width:740px;height:67px;background:#fff}
.logo{position:absolute;left:96px;top:16px;font:700 30px/1 "Roboto Condensed",sans-serif;color:var(--blue);letter-spacing:.5px}
.nav{position:absolute;top:28px;left:310px;height:18px;display:flex;align-items:center;font:400 9.5px "Roboto Condensed",sans-serif;color:#444}
.nav-item{position:absolute;display:flex;align-items:center;gap:3px;white-space:nowrap}
.nav-item svg{width:8px;height:8px;fill:#555}
.pill-sell{left:0;top:0;width:52px;height:17px;border-radius:9px;background:var(--blue);color:#fff;justify-content:center}
.pill-sell svg{fill:#fff}
.pill-register{left:277px;top:-1px;width:59px;height:18px;border-radius:9px;background:var(--green);color:#fff;justify-content:center;font-size:8.5px}
.pill-register svg{fill:#fff}
.sep{position:absolute;top:4px;width:1px;height:10px;background:#ccc}

/* search band */
.search-band{position:absolute;left:0;top:67px;width:740px;height:31px;background:var(--blue)}
.search-field{position:absolute;left:122px;top:5px;width:394px;height:22px;background:#fff;border-radius:11px;display:flex;font-size:7.5px;color:#555}
.search-cat{width:118px;border-right:1px solid #ddd;padding:0 10px;display:flex;align-items:center;justify-content:space-between}
.search-input{padding:0 10px;display:flex;align-items:center;color:#666}
.search-btn{position:absolute;left:526px;top:4px;width:92px;height:23px;border-radius:12px;background:var(--orange);color:#fff;font:400 12px "Roboto Condensed",sans-serif;display:flex;align-items:center;justify-content:center;gap:5px}
.search-btn svg{width:10px;height:10px}

/* hero */
.hero{position:absolute;left:0;top:98px;width:740px;height:272px;background:linear-gradient(90deg,#fbe6f5 0%,#f8d9ef 45%,#f3c6e6 100%);overflow:hidden}
.hero-photo{position:absolute;left:340px;top:0;width:400px;height:272px;background:radial-gradient(circle at 40% 45%,#d9a48c 0%,#b98a7a 18%,#4a3d5a 36%,rgba(243,198,230,0) 62%),linear-gradient(90deg,rgba(248,217,239,0),#f2b8df)}
.hero-kicker{position:absolute;left:93px;top:60px;font:300 27px/1 "Roboto",sans-serif;color:#2a2a2a;letter-spacing:.3px}
.hero-offer{position:absolute;left:91px;top:90px;font:300 66px/1 "Roboto",sans-serif;letter-spacing:-1px}
.hero-offer .pct{color:var(--orange)}
.hero-offer .off{color:var(--blue)}
.hero-sub{position:absolute;left:93px;top:158px;font:300 19px/1 "Roboto",sans-serif;color:#2a2a2a}
.btn-shop{position:absolute;left:94px;top:187px;width:100px;height:26px;border-radius:13px;background:linear-gradient(var(--green),var(--green-dark));color:#fff;font:400 12px "Roboto",sans-serif;display:flex;align-items:center;justify-content:center;gap:4px}
.btn-shop svg{width:9px;height:9px;fill:#fff}

/* intro */
.section-title{position:absolute;left:0;width:740px;text-align:center;font:300 31px/1 "Roboto Condensed",sans-serif;color:var(--blue)}
.section-title b{font-weight:700;color:var(--blue-dark)}
.intro-photo{position:absolute;left:114px;top:452px;width:242px;height:133px;background:linear-gradient(90deg,#f3c2d8,#c9938a 35%,#4a3430 60%,#f0bfd5);border:1px solid #eee}
.intro-heading{position:absolute;left:379px;top:449px;font:300 13px "Roboto",sans-serif;color:var(--blue)}
.intro-text{position:absolute;left:379px;top:470px;width:242px;font-size:7.8px;line-height:12px;color:#555}
.btn-learn{position:absolute;left:379px;top:561px;width:78px;height:18px;border-radius:9px;background:var(--green);color:#fff;font-size:7.5px;display:flex;align-items:center;justify-content:center}

.products-sub{position:absolute;left:0;top:658px;width:740px;text-align:center;font-size:9px;color:#444}

/* product grid */
.tile{position:absolute;width:131px;height:167px;overflow:hidden}
.tile-caption{position:absolute;left:0;bottom:0;width:100%;height:36px;background:var(--caption);color:#fff;text-align:center}
.tile-name{font:600 10px/1 "Open Sans",sans-serif;margin-top:8px}
.tile-link{font-size:6.5px;margin-top:3px}
.tile-feature{background:var(--blue);color:#fff;text-align:center}
.tile-feature .feature-logo{margin-top:30px;font:700 22px/1 "Roboto Condensed",sans-serif}
.tile-feature .feature-name{margin-top:12px;font:600 10px "Open Sans",sans-serif}
.tile-feature .feature-text{margin:3px auto 0;width:118px;font-size:6.8px;line-height:9px}
.tile-feature .feature-link{margin:7px auto 0;width:69px;height:17px;border:1px solid #fff;font-size:6.5px;display:flex;align-items:center;justify-content:center}

/* footer */
.footer{position:absolute;left:0;top:1082px;width:740px;height:118px;background:var(--footer);color:var(--footer-text)}
.footer h4{position:absolute;font:700 9px "Roboto Condensed",sans-serif;color:#eee}
.footer ul{position:absolute;list-style:none;font-size:6.8px;line-height:13.5px}
.social{position:absolute;left:430px;display:flex;align-items:center;gap:8px;font-size:7px}
.social i{display:block;width:15px;height:15px;border-radius:2px}
.footer-logo{position:absolute;left:548px;top:16px;font:700 26px/1 "Roboto Condensed",sans-serif;color:#555}
.copyright{position:absolute;right:94px;top:69px;text-align:right;font-size:7px;line-height:9px}
</style>
</head>
<body>

<header class="header">
  <div class="logo">Bidwell</div>
  <nav class="nav">
    <span class="nav-item pill-sell"><svg viewBox="0 0 10 10"><path d="M1 1h4l4 4-4 4-4-4z"/></svg>Sell ▾</span>
    <span class="nav-item" style="left:61px;top:4px"><svg viewBox="0 0 10 10"><circle cx="5" cy="3" r="2.4"/><path d="M0 10c0-4 10-4 10 0z"/></svg>Sign Up ▾</span>
    <span class="nav-item" style="left:120px;top:4px"><svg viewBox="0 0 10 10"><path d="M0 3h10l-1.5 6h-7z"/></svg>Basket ▾</span>
    <span class="sep" style="left:172px"></span>
    <span class="nav-item" style="left:180px;top:4px"><svg viewBox="0 0 10 10"><circle cx="5" cy="5" r="5"/></svg>Help</span>
    <span class="sep" style="left:212px"></span>
    <span class="nav-item" style="left:220px;top:4px"><svg viewBox="0 0 10 10"><path d="M0 2h10v6H0z"/></svg>Contact</span>
    <span class="nav-item pill-register"><svg viewBox="0 0 10 10"><circle cx="5" cy="3" r="2.4"/><path d="M0 10c0-4 10-4 10 0z"/></svg>Register</span>
  </nav>
</header>

<div class="search-band">
  <div class="search-field">
    <div class="search-cat"><span>All Categories</span><span>▾</span></div>
    <div class="search-input">Search for a brand,product or specific item</div>
  </div>
  <div class="search-btn"><svg viewBox="0 0 10 10"><circle cx="4" cy="4" r="3" fill="none" stroke="#fff" stroke-width="1.6"/><path d="M6 6l3 3" stroke="#fff" stroke-width="1.8"/></svg>Search</div>
</div>

<section class="hero">
  <div class="hero-photo" role="img" aria-label="Model wearing a diamond necklace, earrings and bracelet on a pink bubble background"></div>
  <div class="hero-kicker">JEWELLERY &amp; BEAUTY</div>
  <div class="hero-offer"><span class="pct">25%</span> <span class="off">OFF</span></div>
  <div class="hero-sub">ONLINE &amp; IN STORE</div>
  <div class="btn-shop"><svg viewBox="0 0 10 10"><path d="M0 3h10l-1.5 6h-7z"/></svg>Shop Now</div>
</section>

<h2 class="section-title" style="top:398px"><b>Hi There</b> Nice to meet you</h2>
<div class="intro-photo" role="img" aria-label="Three women with styled hair against a pink backdrop"></div>
<h3 class="intro-heading">Lets talk about Bidwell</h3>
<p class="intro-text">It is a long established fact that a reader will be distracted by the readable content of a page when looking at its layout. The point of using Lorem Ipsum is that it has a more-or-less normal distribution of letters, as opposed to using 'Content here, content here', making it look like readable English. Many desktop publishing packages and web page editors now use Lorem Ipsum as their default model text.</p>
<div class="btn-learn">Learn More ⟶</div>

<h2 class="section-title" style="top:622px"><b>Top</b> Products</h2>
<p class="products-sub">It is a long established fact that a reader will be distracted by the readable content.</p>

<div class="tile" style="left:94px;top:698px;background:linear-gradient(160deg,#8c8c8c,#c0474f 55%,#3a3a3a)" role="img" aria-label="Fashion category photo of a woman in sunglasses and a scarf">
  <div class="tile-caption"><div class="tile-name">Fashion</div><div class="tile-link">See All Product →</div></div>
</div>
<div class="tile" style="left:235px;top:698px;background:linear-gradient(180deg,#6f9a4a,#c9c2b0 45%,#5c8a3a)" role="img" aria-label="Home and garden category photo of a house with a flower garden">
  <div class="tile-caption"><div class="tile-name">Home &amp; Garden</div><div class="tile-link">See All Product →</div></div>
</div>
<div class="tile tile-feature" style="left:376px;top:698px">
  <div class="feature-logo">Bidwell</div>
  <div class="feature-name">Electricals &amp; Technology</div>
  <div class="feature-text">It is a long established fact that a reader will be distracted by the readable content</div>
  <div class="feature-link">See All Product →</div>
</div>
<div class="tile" style="left:516px;top:698px;background:linear-gradient(180deg,#e8e4de,#bdb6ab 60%,#8a8378)" role="img" aria-label="Collectables category photo of an elegant room with a chandelier">
  <div class="tile-caption"><div class="tile-name">Collectables &amp; Aniques</div><div class="tile-link">See All Product →</div></div>
</div>

<div class="tile" style="left:94px;top:878px;background:linear-gradient(180deg,#f6dff0,#b98a6a 50%,#d9b48a)" role="img" aria-label="Jewellery category photo of a woman wearing gold jewellery">
  <div class="tile-caption"><div class="tile-name">Jewellery &amp; Beauty</div><div class="tile-link">See All Product →</div></div>
</div>
<div class="tile" style="left:235px;top:878px;background:linear-gradient(180deg,#efe9df,#d6cbb9)" role="img" aria-label="Toy category photo of a white teddy bear">
  <div class="tile-caption"><div class="tile-name">Toy</div><div class="tile-link">See All Product →</div></div>
</div>
<div class="tile" style="left:376px;top:878px;background:linear-gradient(180deg,#1c1c1c,#6b6159 55%,#2e4a5a)" role="img" aria-label="Sport category photo of a bowling ball and pins">
  <div class="tile-caption"><div class="tile-name">Sport &amp; Leisure</div><div class="tile-link">See All Product →</div></div>
</div>
<div class="tile" style="left:516px;top:878px;background:linear-gradient(160deg,#d8d8d8,#3a3a3a 45%,#111)" role="img" aria-label="Motors category photo of a sports motorbike">
  <div class="tile-caption"><div class="tile-name">Motors</div><div class="tile-link">See All Product →</div></div>
</div>

<footer class="footer">
  <h4 style="left:94px;top:20px">Site Map</h4>
  <ul style="left:94px;top:34px"><li>Contact</li><li>Terms</li><li>Privacy</li><li>RSS</li></ul>
  <ul style="left:149px;top:34px"><li>About</li><li>News</li><li>Feeds</li></ul>
  <h4 style="left:229px;top:20px">Buy</h4>
  <ul style="left:229px;top:36px"><li>Categories</li><li>Search</li><li>Currency</li><li>Converter</li></ul>
  <h4 style="left:320px;top:20px">Sell</h4>
  <ul style="left:320px;top:36px"><li>Sell New Item</li><li>Sell Bulk Items</li></ul>
  <h4 style="left:430px;top:17px">Follow Us</h4>
  <div class="social" style="top:34px"><i style="background:#3b5a9a"></i>Facepage</div>
  <div class="social" style="top:55px"><i style="background:#2aa3e0"></i>Chirper</div>
  <div class="social" style="top:75px"><i style="background:#d33b2c"></i>Circles</div>
  <div class="footer-logo">Bidwell</div>
  <div class="copyright">Copyright Bidwell ® 2003-13. All<br>rights reserved</div>
</footer>

</body>
</html>
```